Cosmetic oil label design

We need a label for a cosmetic oganic Argan Oil. The oil is organic imported from Morocco, cold pressed without any preservatives. The lable is for our round 30ml Airless Bottle with clear body Matte Gold Cap, Shiny Gold Collar. We want to communicate that our product is organic natural and works for all beauty needs. We want the emphasis on the words No preservatives, additives or perfumes
We have attached a picture of the bottle and our compnay's logo.

the bottle demensions are Width/Front: 33.0mm
Length/Depth: 33.0mm
Height: 115.0mm
Lable demensions: Lenght 4inch, width 1.75inch.

let us know if you need any other information, cheers!

Target Market(s)

Our target customer is mainly women 16-70, and also men or anyone looking to have healthy skin and hair using natural products

Industry/Entity Type

Product

Requirements
Must have
• Front side must have:
- attached logo
-words: Authentic Moroccan Argan Oil, No preservatives, additives or perfumes,
L’Huile d’Argan, Produit du Maroc, Imported from Morocco, 30ml

Back side
-Ingredients: 100% Pure Argania Spinosa (Argan Oil)
-Directions: Message into skin, hair or desired area until completely absorbed
-Manufactured for and distributed by Velora Imports
417 W 92nd street New York , NY 10024
Nice to have
• Would be nice if we can fit the following information in the back of the label

Rich in vitamin E and essential fatty acids,Argan oil has several benefits. It Hydrates and nourishes skin and hair. Can be used for treating dry skin, split ends softening cuticles. It works for all types of skin.

```html
<!DOCTYPE html>
<html lang="en">
<head>
<meta charset="utf-8">
<title>Argan Oil Label – Back</title>
<link href="https://fonts.googleapis.com/css2?family=Gelasio:wght@400;700&display=swap" rel="stylesheet">
<style>
  :root {
    --brown-top: #3b2b14;
    --brown-upper: #6e5122;
    --gold-center: #cf9d45;
    --gold-lower: #ad8545;
    --brown-lower: #5e4b30;
    --brown-bottom: #2d2419;
    --ink: #2a1d10;
  }
  html, body {
    margin: 0;
    padding: 0;
    width: 1200px;
    height: 2743px;
    overflow: hidden;
  }
  .label-back {
    position: relative;
    width: 1200px;
    height: 2743px;
    background: linear-gradient(to bottom,
      var(--brown-top) 0%,
      var(--brown-upper) 24%,
      var(--gold-center) 47%,
      var(--gold-lower) 66%,
      var(--brown-lower) 84%,
      var(--brown-bottom) 100%);
    font-family: "Gelasio", Georgia, serif;
    color: var(--ink);
    text-align: center;
  }
  .label-copy {
    position: absolute;
    top: 1018px;
    left: 0;
    width: 100%;
    font-size: 72px;
    line-height: 75px;
  }
  .label-copy h2 {
    margin: 0;
    font-size: 72px;
    font-weight: 700;
    line-height: 78px;
  }
  .label-copy p {
    margin: 0;
    font-weight: 400;
  }
  .section + .section {
    margin-top: 75px;
  }
</style>
</head>
<body>
  <main class="label-back">
    <div class="label-copy">
      <section class="section ingredients">
        <h2>Ingredients</h2>
        <p>100% Pure Argania Spinosa<br>(Argan Oil)</p>
      </section>
      <section class="section directions">
        <h2>Directions</h2>
        <p>Message into skin, hair or<br>desired area until completely<br>absorbed.</p>
      </section>
      <section class="section distributor">
        <p>Manufactured for and distributed<br>by Velora Imports 417 W 92nd<br>street New York , NY 10024</p>
      </section>
    </div>
  </main>
</body>
</html>
```